I am looking for a Business Card Design for my spirit company titled "Harbor Cask" The company specializes in prohibition style/speakeasy mixology drinks and alcohol distribution. I am looking for Retro, Masculine, Sophisticated Card that embodies the look of Prohibition. Black and White colors. Also add Chatterly, Pictoro logo

Information that should go on the card is my Name, Title, Phone, Email, Website as follows:

Tobias R Grendle
Principal
415.867.2290
tobias@harborcask.com
harborcask.com
Updates

Hello all I have uploaded a pdf version of the logo. It seems as if some are saying the resolution is too small.

Target Market(s)

Male and Female drinkers of all ages with a sophisticated palate that have an appreciation for fine crafted cocktail

Industry/Entity Type

Business

Requirements
Must have
• Information that should go on the card is my Name, Title, Phone, Email, Website as follows:

Tobias R Grendle
Principal
415.867.2290
tobias@harborcask.com
harborcask.com

```html
<!DOCTYPE html>
<html lang="en">
<head>
<meta charset="utf-8">
<title>Harbor Cask – Business Card</title>
<link rel="stylesheet" href="https://fonts.googleapis.com/css2?family=Lato:wght@400;700;900&display=swap">
<style>
  :root {
    --stage: #2a2a2a;
    --card: #141414;
    --card-light: #1c1c1c;
    --ink: #ffffff;
    --ink-dark: #111111;
    --ribbon-fold: #9a9a9a;
    --ribbon-tail: #d9d9d9;
  }
  * { margin: 0; padding: 0; box-sizing: border-box; }
  html, body {
    width: 1200px; height: 900px; overflow: hidden;
    background: var(--stage);
    font-family: "Lato", sans-serif;
    color: var(--ink);
  }
  .stage { position: relative; width: 1200px; height: 900px; }
  .card {
    position: absolute; top: 135px;
    width: 360px; height: 630px;
    background: linear-gradient(160deg, var(--card-light), var(--card));
    overflow: hidden;
  }
  .card--front { left: 190px; }
  .card--back { left: 650px; }

  /* Front */
  .brand {
    position: absolute; left: 0; right: 0; top: 290px;
    display: flex; justify-content: center; align-items: center; gap: 14px;
  }
  .brand__dot {
    width: 16px; height: 16px; border-radius: 50%;
    background: var(--ink);
  }
  .brand__name { font-weight: 400; font-size: 42px; letter-spacing: 1px; }

  /* Back */
  .band { position: absolute; left: 0; top: 0; }
  .ribbon { position: absolute; left: 0; top: 322px; }
  .contact {
    position: absolute; left: 0; right: 0; top: 390px;
    text-align: center;
  }
  .contact__title { font-size: 19px; font-weight: 700; letter-spacing: 1.5px; }
  .contact__phone { margin-top: 22px; font-size: 35px; font-weight: 400; letter-spacing: 1px; }
  .contact__line { margin-top: 4px; font-size: 20px; font-weight: 400; letter-spacing: 0.5px; }
  .social {
    margin-top: 30px;
    display: flex; justify-content: center; align-items: center; gap: 16px;
    font-size: 18px; font-weight: 400;
  }
  .social__name { font-weight: 700; }
</style>
</head>
<body>
<main class="stage">

  <section class="card card--front" aria-label="Card front">
    <div class="brand">
      <span class="brand__dot"></span>
      <span class="brand__name">Harbor Cask</span>
    </div>
  </section>

  <section class="card card--back" aria-label="Card back">
    <svg class="band" width="360" height="360" viewBox="0 0 360 360">
      <polygon points="125,0 240,0 240,330 182,296 125,330" fill="var(--ink)"/>
    </svg>

    <svg class="ribbon" width="360" height="60" viewBox="0 0 360 60">
      <polygon points="18,14 60,14 60,46 18,46 32,30" fill="var(--ribbon-tail)"/>
      <polygon points="342,24 300,24 300,56 342,56 328,40" fill="var(--ribbon-tail)"/>
      <polygon points="48,46 60,46 60,54" fill="var(--ribbon-fold)"/>
      <polygon points="312,14 300,14 300,24" fill="var(--ribbon-fold)"/>
      <polygon points="48,6 312,14 312,54 48,46" fill="var(--ink)"/>
      <text x="180" y="38" text-anchor="middle" font-family="Lato, sans-serif" font-weight="900" font-size="17" letter-spacing="0.5" fill="var(--ink-dark)" transform="rotate(1.7 180 30)">TOBIAS R. GRENDLE</text>
    </svg>

    <div class="contact">
      <p class="contact__title">Principal</p>
      <p class="contact__phone">415.867.2290</p>
      <p class="contact__line">tobias@harborcask.com</p>
      <p class="contact__line">www.harborcask.com</p>
      <p class="social">
        <span>Join us at:</span>
        <span class="social__name">Pictoro</span>
        <span class="social__name">Chatterly</span>
      </p>
    </div>
  </section>

</main>
</body>
</html>
```